Gutschein-Design für Tätowierer
Zielgruppe
Ich bin ein Tätowierer und suche ein hochwertiges Design, meine Zielgruppe sind Leute jeden Alters
Aufgabenstellung
-Farbe auf meiner Karte sollte wie bei meiner Webseite www.brenno-tattoo.de sein Pazifikblau/ Marineblau
-Es soll schlicht sein
-mein Logo soll auf die Vorderseite mittig (in schwarz)
-ein Rand soll enthalten sein in einem blauton
-auf die Rückseite sollen Felder zum ausfüllen sein wie zum Beispiel Name, Gutschein wert usw..
-Maße ca. 21 x 10,5 cm

```html
<!DOCTYPE html>
<html lang="de">
<head>
<meta charset="utf-8">
<title>Tattoo Gutschein – Varnik Ink</title>
<link rel="stylesheet" href="https://fonts.googleapis.com/css2?family=Barlow:wght@400;600;700&family=Caveat+Brush&family=DM+Serif+Display&display=swap">
<style>
  :root {
    --navy: #2a4169;
    --ink: #050505;
    --paper: #ffffff;
    --label: #2b2b2b;
    --stage: #d9dadd;
    --photo-light: #8b8b8b;
    --photo-mid: #4a4a4a;
  }
  * { margin: 0; padding: 0; box-sizing: border-box; }
  html, body { width: 1200px; height: 800px; overflow: hidden; }
  body {
    background: var(--stage);
    font-family: "Barlow", sans-serif;
    position: relative;
  }
  .voucher {
    position: absolute;
    left: 240px;
    width: 720px;
    height: 360px;
    background: var(--navy);
  }
  .voucher--front { top: 24px; }
  .voucher--back { top: 412px; }

  .voucher__inner {
    position: absolute;
    left: 18px; top: 18px; right: 18px; bottom: 18px;
    background: var(--ink);
    overflow: hidden;
  }
  .voucher--back .voucher__inner { bottom: 34px; }

  /* Front */
  .front-photo {
    position: absolute;
    right: 0; top: 0; bottom: 0;
    width: 56%;
    background: linear-gradient(90deg, var(--ink) 0%, #2a2a2a 30%, var(--photo-mid) 65%, var(--photo-light) 100%);
  }
  .title {
    position: absolute;
    left: 120px; top: 78px;
    color: var(--paper);
    text-align: center;
    width: 360px;
  }
  .title__small {
    font-family: "DM Serif Display", serif;
    font-size: 48px;
    line-height: 1;
    display: block;
    margin-left: 90px;
  }
  .title__large {
    font-family: "Caveat Brush", cursive;
    font-size: 118px;
    line-height: 0.95;
    display: block;
  }
  .brand {
    position: absolute;
    display: flex;
    align-items: center;
    gap: 8px;
    color: var(--paper);
    font-family: "Barlow", sans-serif;
    font-weight: 700;
  }
  .brand__dot {
    border-radius: 50%;
    border: 2px solid var(--paper);
    flex: none;
  }
  .brand--front { right: 24px; top: 26px; font-size: 22px; }
  .brand--front .brand__dot { width: 18px; height: 18px; }

  /* Back */
  .back-photo {
    position: absolute;
    left: 0; top: 0; bottom: 0;
    width: 50%;
    background: linear-gradient(90deg, #9a9a9a 0%, #6e6e6e 40%, #3a3a3a 75%, var(--ink) 100%);
  }
  .brand--back { left: 70px; top: 140px; font-size: 38px; }
  .brand--back .brand__dot { width: 30px; height: 30px; border-width: 3px; }

  .contact {
    position: absolute;
    left: 352px; top: 22px;
    display: flex;
    gap: 22px;
    color: var(--paper);
    font-weight: 700;
    font-size: 15px;
  }
  .contact__item { display: flex; align-items: center; gap: 8px; }
  .contact__icon {
    width: 22px; height: 22px;
    border-radius: 50%;
    background: var(--navy);
    flex: none;
  }
  .fields {
    position: absolute;
    left: 352px; right: 20px; top: 62px;
    display: flex;
    flex-direction: column;
    gap: 14px;
  }
  .field {
    height: 58px;
    background: var(--paper);
    display: flex;
    align-items: center;
    padding-left: 22px;
    color: var(--label);
    font-weight: 700;
    font-size: 16px;
  }
  .voucher__note {
    position: absolute;
    left: 18px; right: 18px; bottom: 9px;
    text-align: center;
    color: var(--paper);
    font-size: 11px;
    letter-spacing: 0.2px;
  }
</style>
</head>
<body>

  <section class="voucher voucher--front">
    <div class="voucher__inner">
      <div class="front-photo" role="img" aria-label="Schwarzweißfoto: Tätowierer mit Handschuhen bei der Arbeit"></div>
      <h1 class="title">
        <span class="title__small">Tattoo</span>
        <span class="title__large">Gutschein</span>
      </h1>
      <div class="brand brand--front"><span class="brand__dot"></span>Varnik Ink</div>
    </div>
  </section>

  <section class="voucher voucher--back">
    <div class="voucher__inner">
      <div class="back-photo" role="img" aria-label="Schwarzweißfoto einer Marienskulptur und eines gestochenen Tattoos derselben Figur"></div>
      <div class="brand brand--back"><span class="brand__dot"></span>Varnik Ink</div>

      <div class="contact">
        <div class="contact__item"><span class="contact__icon"></span>varnik_ink</div>
        <div class="contact__item"><span class="contact__icon"></span>www.brenno-tattoo.de</div>
      </div>

      <div class="fields">
        <div class="field">Betrag :</div>
        <div class="field">Für :</div>
        <div class="field">Gültig Bis :</div>
      </div>
    </div>
    <p class="voucher__note">Eine Barauszahlung ist nicht möglich. Terminvereibarungen bitte bitte unter 0987 / 65 43 21 10</p>
  </section>

</body>
</html>
```